Pause Your Day And Browse- PYDB poster

I am the Vice President of Advocacy for the Coastline Shelfkeepers Guild. I am looking to have a set of posters made for PYDB (Pause Your Day and Browse) October 23. PYDB is a time when all school children in BC are encouraged to Pause Your Day and Browse for 15-20 minutes at some point in their day.

I would like to get a set of 2 digital posters designed (if possible it would be nice to have the option to print to both 11 x 17 and 8.5 x 11 paper). We need a poster that is high school (Grade 8-12) appropriate and one that is elementary (Grade k-7) appropriate. Both posters need to be replicated in French. All posters need to have the KWNU logo on them as well as the Coastline Shelfkeepers Guild Logo.

Here is a link to last year's successful design http://kwnu-example.org/csg/info/advocacy.html
There are two additional samples in the uploaded files section.

Each poster needs to have the following information:

-Pause Your Day and Browse (PYDB)
- The date Monday, October 23, 2017
-the logo for the KWNU (attached)
-the logo for the CSG (attached)- the logos do not have to be large.

Target Market(s)

Children ages 5-12 and 12-17 as well as their teachers

Industry/Entity Type

Teacher

Font styles to use
Sans Serif

Requirements
Must have
• Must have both logos- colours may be changed for either or both
Nice to have
• Clear, Bright lettering. Images of child or children enjoying reading
Should not have
• stereotypes

```html
<!DOCTYPE html>
<html lang="en">
<head>
<meta charset="utf-8">
<title>PYDB – Pause Your Day And Browse</title>
<link rel="stylesheet" href="https://fonts.googleapis.com/css2?family=Open+Sans:wdth,wght@75,300;75,400;100,400;100,700&display=swap">
<style>
  :root {
    --paper: #f7f8f9;
    --paper-shade: #e9ebee;
    --rule-blue: #b9c6e4;
    --margin-red: #e7a3a8;
    --green-light: #62b02e;
    --green-dark: #3f7a1b;
    --ink: #111111;
    --frame-blue: #2c4d8e;
    --photo-light: #dfe3f3;
    --photo-mid: #6a6fc0;
    --badge-blue: #2c4d8e;
  }
  * { margin: 0; padding: 0; box-sizing: border-box; }
  html, body { width: 848px; height: 1200px; overflow: hidden; background: #ffffff; }
  .poster {
    position: relative;
    width: 848px;
    height: 1200px;
    overflow: hidden;
    font-family: "Open Sans", sans-serif;
    background:
      linear-gradient(180deg, rgba(255,255,255,0) 78%, var(--paper-shade) 100%),
      repeating-linear-gradient(180deg, transparent 0 20px, var(--rule-blue) 20px 21px),
      var(--paper);
  }
  .poster::before {
    content: "";
    position: absolute;
    left: 70px; top: 0; bottom: 0;
    width: 1px;
    background: var(--margin-red);
  }
  .headline { position: absolute; left: 0; top: 0; width: 848px; height: 470px; }
  .headline__acronym { font-family: "Open Sans", sans-serif; font-stretch: 75%; font-weight: 300; }
  .headline__full { font-family: "Open Sans", sans-serif; font-stretch: 75%; font-weight: 300; fill: var(--ink); }
  .photo {
    position: absolute;
    left: 122px; top: 540px;
    width: 618px; height: 424px;
    border: 10px solid var(--frame-blue);
    transform: rotate(-3deg);
    background: radial-gradient(ellipse at 55% 55%, var(--photo-mid) 0%, #9ea3d8 40%, var(--photo-light) 80%);
  }
  .guild-mark {
    position: absolute;
    left: 48px; top: 1044px;
    width: 124px; height: 128px;
    background: #ffffff;
    display: flex; flex-direction: column; align-items: center; justify-content: center;
    gap: 8px;
  }
  .guild-mark__name { font-size: 40px; font-weight: 700; color: var(--ink); line-height: 1; }
  .guild-mark__caption { font-size: 7.5px; font-weight: 400; text-align: center; line-height: 1.25; color: var(--ink); }
  .event-date {
    position: absolute;
    left: 196px; top: 1092px;
    font-size: 18px; font-weight: 700;
    letter-spacing: 5px;
    color: var(--ink);
  }
  .union-mark {
    position: absolute;
    right: 40px; top: 1083px;
    display: flex; align-items: center; gap: 8px;
  }
  .union-mark__dot { width: 30px; height: 30px; border-radius: 50%; background: var(--badge-blue); }
  .union-mark__name { font-size: 26px; font-weight: 700; color: var(--badge-blue); }
</style>
</head>
<body>
<main class="poster">
  <svg class="headline" viewBox="0 0 848 470" aria-label="PYDB – Pause Your Day And Browse">
    <defs>
      <linearGradient id="titleGreen" x1="0" x2="1" y1="0" y2="1">
        <stop offset="0" stop-color="var(--green-light)"/>
        <stop offset="1" stop-color="var(--green-dark)"/>
      </linearGradient>
    </defs>
    <text class="headline__acronym" x="76" y="400" font-size="492" fill="url(#titleGreen)"
          textLength="726" lengthAdjust="spacingAndGlyphs">PYDB</text>
    <text class="headline__full" x="64" y="458" font-size="56"
          textLength="736" lengthAdjust="spacingAndGlyphs">PAUSE YOUR DAY AND BROWSE</text>
  </svg>

  <div class="photo" role="img" aria-label="Two young children sitting cross-legged in front of bookshelves, one reading a comic book, tinted blue"></div>

  <div class="guild-mark">
    <span class="guild-mark__name">CSG</span>
    <span class="guild-mark__caption">COASTLINE<br>SHELFKEEPERS<br>GUILD</span>
  </div>

  <p class="event-date">MONDAY, OCTOBER 23, 2017</p>

  <div class="union-mark">
    <span class="union-mark__dot"></span>
    <span class="union-mark__name">KWNU</span>
  </div>
</main>
</body>
</html>
```